Cool blackchain based app company needs a website :)

pillcheckhub.net

Kinda says it all!! This is an app which sits on your smartfone / tablet. You scan a QR code from a medicinal product and our app will verify if the product you have is genuine. It's simple, It's free.

The design could be very modern and simple. It should show in graphical form how the app works and have FAQ's etc.

pillcheckhub.net is designed specifically to allow consumers verify that the medical products which they have purchased are genuine.

Detailed brief with content attached. Logo in high res and QR code attached.

Full website required.
Updates

Target Market(s)

Pharmaceutical

Industry/Entity Type

Pharmaceutical

Coding

Coded - Design and coding required

Number of Pages Required

3 page

Colors

Designer to choose colors to be used in the design.

Requirements
Must have
• Strong visuals - very simple navigation - 3 pages
Nice to have
• Animation of the process
Should not have
• Jargon!

```html
<!DOCTYPE html>
<html lang="en">
<head>
<meta charset="utf-8">
<title>pillcheckhub.net</title>
<link href="https://fonts.googleapis.com/css2?family=Open+Sans:wght@400;600;700&family=Abril+Fatface&display=swap" rel="stylesheet">
<style>
:root{
  --brand-blue:#1a7fd0;
  --teal:#127f94;
  --panel-blue:#2f7fcf;
  --nav-blue:#1b77c5;
  --ink:#222;
  --grey-text:#666;
  --card-grey:#e4e4e4;
  --white:#fff;
  --black:#000;
  --footer:#080808;
}
*{box-sizing:border-box;margin:0;padding:0}
html,body{width:707px;height:1200px;overflow:hidden;background:var(--white);font-family:"Open Sans",Arial,sans-serif;color:var(--ink)}
.page{position:relative;width:707px;height:1200px}
.abs{position:absolute}

/* header */
.site-header{left:71px;top:0;width:564px;height:58px;background:linear-gradient(#fff,#f1f1f1)}
.brand{left:45px;top:12px;display:flex;align-items:center;gap:6px;font-size:11px;font-weight:700;color:var(--nav-blue)}
.brand-dot{width:28px;height:28px;border-radius:50%;background:var(--brand-blue)}
.main-nav{left:306px;top:23px;display:flex;gap:10px;font-size:5.5px;font-weight:700;color:var(--nav-blue)}
.social{left:472px;top:20px;display:flex;gap:3px}
.social span{width:11px;height:11px;border-radius:50%;border:1px solid #ccc;background:#fff}

/* hero / faq */
.hero-photo{left:71px;top:58px;width:564px;height:268px;background:linear-gradient(100deg,#b7bcc0 0%,#e6e8ea 35%,#cfd5d9 60%,#eef0f1 80%,#c9c3c3 100%)}
.faq-title{left:71px;top:100px;width:564px;text-align:center;font-family:"Abril Fatface",serif;font-size:16px;color:var(--white)}
.faq-panel{left:108px;top:134px;width:483px;height:141px;background:var(--panel-blue);opacity:.95}
.faq-item{position:absolute;background:#f3f3f3;border-radius:2px;font-size:5.6px;color:var(--nav-blue);padding:0 12px 0 4px;display:flex;align-items:center;line-height:1.5}
.faq-item::after{content:"";position:absolute;right:4px;top:50%;margin-top:-2.5px;border-left:3px solid var(--nav-blue);border-top:2.5px solid transparent;border-bottom:2.5px solid transparent}

/* about */
.section-title{width:707px;left:0;text-align:center;color:var(--teal);font-size:16px}
.about-quote{left:150px;top:413px;width:386px;height:109px;border-left:2px solid #ccc;padding-left:10px}
.about-lead{font-size:8px;line-height:1.4;color:var(--ink)}
.about-body{font-size:6.2px;font-weight:700;line-height:1.45;color:var(--grey-text);margin-top:6px}
.founder-card{position:absolute;top:580px;width:163px;height:244px;background:var(--card-grey);border-radius:14px;text-align:center}
.founder-photo{position:absolute;left:50%;width:66px;height:66px;margin-left:-33px;border-radius:50%;border:2px solid #fff;background:radial-gradient(#9a8e88,#4d4a49)}
.founder-name{position:absolute;left:10px;width:142px;height:16px;background:var(--black);color:var(--brand-blue);font-size:11px;line-height:16px}
.founder-name.serif{font-family:"Abril Fatface",serif;font-size:11px}
.founder-role{position:absolute;width:100%;font-family:"Abril Fatface",serif;font-size:8px;color:var(--nav-blue)}
.founder-bio{position:absolute;left:10px;width:140px;text-align:left;font-size:6.2px;line-height:1.45;color:var(--grey-text)}

/* contact */
.contact-photo{left:71px;top:876px;width:564px;height:273px;background:linear-gradient(100deg,#b3b8bb 0%,#e5e7e9 35%,#d3d8db 60%,#eceeef 80%,#c6c0c0 100%)}
.contact-title{left:114px;top:902px;font-size:12px;font-weight:700;color:var(--ink)}
.field-label{position:absolute;font-size:5.5px;color:#777}
.field{position:absolute;background:var(--white);border:1px solid #ddd}
.send-btn{left:114px;top:1100px;width:65px;height:18px;background:var(--brand-blue);color:#fff;font-size:7.5px;border-radius:2px;display:flex;align-items:center;justify-content:center}

/* footer */
.site-footer{left:71px;top:1166px;width:564px;height:33px;background:var(--footer)}
.footer-brand{left:53px;top:10px;display:flex;align-items:center;gap:3px;font-size:5px;color:var(--brand-blue)}
.footer-brand i{width:10px;height:10px;border-radius:50%;background:var(--brand-blue)}
.copyright{right:50px;top:13px;font-size:5px;color:#555}
</style>
</head>
<body>
<div class="page">

  <header class="site-header abs">
    <div class="brand abs"><span class="brand-dot"></span>pillcheckhub.net</div>
    <nav class="main-nav abs"><span>HOME</span><span>ABOUT US</span><span>FAQS</span><span>HOW TO USE</span><span>CONTACT</span></nav>
    <div class="social abs" aria-label="Social links"><span></span><span></span><span></span></div>
  </header>

  <section>
    <div class="hero-photo abs" role="img" aria-label="Blurred photo of a scientist working in a pharmaceutical laboratory"></div>
    <h1 class="faq-title abs">Frequently Asked Questions</h1>
    <div class="faq-panel abs">
      <div class="faq-item" style="left:16px;top:8px;width:218px;height:18px">How does it work?</div>
      <div class="faq-item" style="left:16px;top:32px;width:218px;height:18px">So, will pillcheckhub keep a log of the medicines I take???</div>
      <div class="faq-item" style="left:16px;top:55px;width:218px;height:25px">OK, they can't create genuine pillcheckhub.net QR codes, but what is to stop a fraudster simply copying a genuine code??</div>
      <div class="faq-item" style="left:16px;top:87px;width:218px;height:18px">Will I be hounded by ads??</div>
      <div class="faq-item" style="left:16px;top:111px;width:218px;height:18px">Who pays for this then?</div>
      <div class="faq-item" style="left:249px;top:20px;width:219px;height:18px">What's to stop a fraudster creating their own QR codes??</div>
      <div class="faq-item" style="left:249px;top:44px;width:219px;height:27px">A unique code for every packet of medicine?? Surely this is impossible?</div>
      <div class="faq-item" style="left:249px;top:77px;width:219px;height:18px">How much does this cost me??</div>
      <div class="faq-item" style="left:249px;top:100px;width:219px;height:18px">Will you resell any of my information??</div>
    </div>
  </section>

  <section>
    <h2 class="section-title abs" style="top:380px;font-weight:400">ABOUT US</h2>
    <div class="about-quote abs">
      <p class="about-lead">Founded by two long time and highly experienced friends, Daniel Hartwell and Marcus Delacroix, pillcheckhub.net is dedicated to reducing the number of people who suffer due to counterfeit medical products.</p>
      <p class="about-body">The pharmaceutical industry is leading the way in terms of investing in anti-counterfeiting solutions to protect consumers. However, counterfeit medicine is a huge business, estimated to be worth over €100 billion annually.</p>
      <p class="about-body">Using their combined knowledge and experience in the data security and anti-fraud industries, Daniel and Marcus have developed a (patent pending) highly secure, fast and free solution to protecting people against counterfeit medicines.</p>
    </div>
    <h2 class="section-title abs" style="top:537px;font-weight:400">The Founders</h2>

    <article class="founder-card" style="left:154px">
      <div class="founder-photo" style="top:21px" role="img" aria-label="Portrait photo of Daniel Hartwell"></div>
      <div class="founder-name" style="top:100px">Daniel Hartwell</div>
      <div class="founder-role" style="top:129px">CEO</div>
      <p class="founder-bio" style="top:147px">Daniel is a global business leader who has been on the founding team of a number of software companies, leading with patented solutions. Daniel has a proven reputation and ability to 'start from scratch' in new markets, developing sales, marketing and delivery organizations.</p>
    </article>

    <article class="founder-card" style="left:350px">
      <div class="founder-photo" style="top:12px" role="img" aria-label="Portrait photo of Marcus Delacroix"></div>
      <div class="founder-name serif" style="top:91px">Marcus Delacroix</div>
      <div class="founder-role" style="top:120px">CIO</div>
      <p class="founder-bio" style="top:138px">Marcus is a highly experienced technologist, innovator, visionary and entrepreneur specializing in Architectural and Network Security, Blockchain Deployments, Distributed Architecture and Cloud Computing. Marcus has over twenty-five years of professional experience, with the last fifteen as founder and CEO of a number of IT and Software companies.</p>
    </article>
  </section>

  <section>
    <div class="contact-photo abs" role="img" aria-label="Blurred photo of a scientist in a pharmaceutical laboratory"></div>
    <h2 class="contact-title abs">Contact Us</h2>
    <span class="field-label" style="left:114px;top:924px">Your name *</span>
    <div class="field" style="left:114px;top:934px;width:229px;height:14px"></div>
    <span class="field-label" style="left:356px;top:924px">Your email address *</span>
    <div class="field" style="left:356px;top:934px;width:229px;height:14px"></div>
    <span class="field-label" style="left:114px;top:956px">Subject</span>
    <div class="field" style="left:114px;top:966px;width:471px;height:14px"></div>
    <span class="field-label" style="left:114px;top:988px">Your Message</span>
    <div class="field" style="left:114px;top:998px;width:471px;height:95px"></div>
    <div class="send-btn abs">Send Message</div>
  </section>

  <footer class="site-footer abs">
    <div class="footer-brand abs"><i></i>pillcheckhub.net</div>
    <div class="copyright abs">© Copyright 2017. All Rights Reserved.</div>
  </footer>

</div>
</body>
</html>
```